Stationary

We have designed a new logo and business care.
It is now time for stationary.
We are a financial planning firm and are looking for something more formal that show the strength of our firm.
Please include our tag line; Integrity - Vision -Diligence.
I have uploaded a PDF of our current stationary - but - you are under no obligation to design anything like it.
Thx
Marta
Business

```html
<!DOCTYPE html>
<html lang="en">
<head>
<meta charset="utf-8">
<title>Halden Crest Group Stationery</title>
<link rel="stylesheet" href="https://fonts.googleapis.com/css2?family=Montserrat:wght@400;500;600&display=swap">
<style>
  :root {
    --navy: #283a8f;
    --sky: #1676bd;
    --white: #ffffff;
    --ink: #444a55;
    --backdrop: #e9eaec;
  }
  html, body {
    margin: 0;
    padding: 0;
    width: 1200px;
    height: 872px;
    overflow: hidden;
    background: var(--backdrop);
    font-family: "Montserrat", sans-serif;
  }
  .canvas { position: relative; width: 1200px; height: 872px; }
  .sheet { position: absolute; background: var(--white); box-shadow: 6px 8px 14px rgba(0,0,0,0.18); overflow: hidden; }
  .letterhead { left: 70px; top: 64px; width: 574px; height: 742px; }
  .card-front { left: 708px; top: 218px; width: 359px; height: 205px; }
  .card-back { left: 708px; top: 448px; width: 359px; height: 205px; background: var(--navy); }
  .abs { position: absolute; margin: 0; white-space: nowrap; }
  .brand-name { color: var(--navy); font-weight: 400; }
  .tagline { color: var(--ink); font-size: 6.5px; letter-spacing: 2.6px; font-weight: 500; }
  .letterhead .brand-name { right: 24px; top: 68px; font-size: 16px; }
  .letterhead .tagline { right: 22px; top: 88px; }
  .header-rule { position: absolute; left: 70px; top: 94px; width: 300px; height: 2px; background: var(--navy); }
  .wave { position: absolute; left: 0; bottom: 0; display: block; }
  .contact { color: var(--white); font-size: 9.5px; line-height: 11.5px; }
  .holder-name { color: var(--white); font-weight: 600; font-size: 13px; }
  .holder-role { color: var(--white); font-size: 9px; }
  .letterhead .holder-name { right: 24px; top: 676px; }
  .letterhead .holder-role { right: 24px; top: 693px; }
  .letterhead .address { left: 80px; top: 710px; }
  .letterhead .phones { right: 24px; top: 710px; text-align: right; }
  .card-front .brand-name { left: 0; right: 0; text-align: center; top: 58px; font-size: 12.5px; }
  .card-front .tagline { left: 0; right: 0; text-align: center; top: 76px; font-size: 5px; letter-spacing: 2px; }
  .card-front .holder-name { left: 53px; top: 158px; font-size: 12px; }
  .card-front .holder-role { left: 53px; top: 175px; font-size: 8.5px; border-bottom: 1px solid var(--white); width: 95px; padding-bottom: 1px; }
  .card-front .phones { right: 16px; top: 156px; text-align: right; font-size: 8.8px; line-height: 11px; }
  .card-front .address { right: 16px; top: 182px; text-align: right; font-size: 8.8px; line-height: 11px; }
  .icon { display: inline-block; width: 7px; height: 7px; margin-left: 4px; vertical-align: -0.5px; }
  .card-back .brand-name { left: 0; right: 0; top: 88px; text-align: center; color: var(--white); font-size: 22px; }
</style>
</head>
<body>
<div class="canvas">

  <section class="sheet letterhead" aria-label="Letterhead">
    <p class="abs brand-name">Halden Crest Group</p>
    <p class="abs tagline">Clarity Focus Steadiness</p>
    <div class="header-rule"></div>

    <svg class="wave" width="574" height="122" viewBox="0 0 574 122" aria-hidden="true">
      <path d="M0,122 L0,70 C60,32 190,12 300,12 C420,12 520,30 574,52 L574,122 Z" fill="var(--sky)"/>
      <path d="M72,122 C48,100 66,60 200,45 C320,30 470,36 574,56 L574,122 Z" fill="var(--navy)"/>
      <path d="M72,122 C48,100 66,60 200,45 C320,30 470,36 574,56" fill="none" stroke="var(--white)" stroke-width="1"/>
    </svg>

    <p class="abs holder-name">Marta Kelly</p>
    <p class="abs holder-role">Director</p>
    <p class="abs contact address">2270 W. Alder Ave.,<br>Riverton, WA 99012</p>
    <p class="abs contact phones">
      (555) 014-2231<svg class="icon" viewBox="0 0 10 10" aria-hidden="true"><path d="M2,1 L4,1 L4.6,3 L3.4,4 C4,5.4 4.8,6.2 6,6.6 L7,5.4 L9,6 L9,8 C5,8.6 1.4,5 2,1 Z" fill="var(--white)"/></svg><br>
      (555) 014-2239<svg class="icon" viewBox="0 0 10 10" aria-hidden="true"><rect x="3" y="1" width="4" height="3" fill="var(--white)"/><rect x="1" y="4" width="8" height="4" rx="1" fill="var(--white)"/><rect x="3" y="7" width="4" height="2" fill="var(--white)"/></svg>
    </p>
  </section>

  <section class="sheet card-front" aria-label="Business card front">
    <p class="abs brand-name">Halden Crest Group</p>
    <p class="abs tagline">Clarity Focus Steadiness</p>

    <svg class="wave" width="359" height="205" viewBox="0 0 359 205" aria-hidden="true">
      <path d="M0,205 L0,170 C10,120 90,95 200,94 C270,94 330,115 359,138 L359,205 Z" fill="var(--sky)"/>
      <path d="M42,205 C30,170 60,130 170,120 C250,114 320,125 359,140 L359,205 Z" fill="var(--navy)"/>
      <path d="M42,205 C30,170 60,130 170,120 C250,114 320,125 359,140" fill="none" stroke="var(--white)" stroke-width="1"/>
    </svg>

    <p class="abs holder-name">Marta Kelly</p>
    <p class="abs holder-role">Director</p>
    <p class="abs contact phones">
      (555) 014-2231<svg class="icon" viewBox="0 0 10 10" aria-hidden="true"><path d="M2,1 L4,1 L4.6,3 L3.4,4 C4,5.4 4.8,6.2 6,6.6 L7,5.4 L9,6 L9,8 C5,8.6 1.4,5 2,1 Z" fill="var(--white)"/></svg><br>
      (555) 014-2239<svg class="icon" viewBox="0 0 10 10" aria-hidden="true"><rect x="3" y="1" width="4" height="3" fill="var(--white)"/><rect x="1" y="4" width="8" height="4" rx="1" fill="var(--white)"/><rect x="3" y="7" width="4" height="2" fill="var(--white)"/></svg>
    </p>
    <p class="abs contact address">2270 W. Alder Ave.,<br>Riverton, WA 99012</p>
  </section>

  <section class="sheet card-back" aria-label="Business card back">
    <p class="abs brand-name">Halden Crest Group</p>
  </section>

</div>
</body>
</html>
```